The Amber Tides (celtic rap album by Oskar Venlow)

Peace. I'm Oskar Venlow, I make celtic/druidic/pagan rap music. The album is called ' The Amber Tides ' which has to do with celtic cosmology: The Underworld (The Sea) is the realms of the past, the ancestors, trauma, transformation, knowledge of the old ways ... ; This World (The Land) is the realm of ordinary reality, our life, the present, skills, fertility ... ; and The Upperworld (The Sky) which is the realm of the gods, the future, goals, planning of harvest.... Three was a sacred number and describes the fullness of life and is symbolized by the triskele, e.g. found at Dunmorrow.

I have no idea for a cover lol, so go wild. It would be good if the three worlds are somehow featured.

This is one of the songs: https://www.clipvault-example.net/watch?v=qRtLmnWXpZA

Target Market(s)

pagans, spiritual people

Requirements
Must have
• something that references The Amber Tides (see description)
Nice to have
• Celtic symbol(s); contrasts between light and dark; past - present - future

```html
<!DOCTYPE html>
<html lang="en">
<head>
<meta charset="utf-8">
<title>Oskar Venlow – The Amber Tides</title>
<link rel="stylesheet" href="https://fonts.googleapis.com/css2?family=Permanent+Marker&display=swap">
<style>
  :root {
    --paper: #f3f2f0;
    --paper-shade: #e6e5e3;
    --ink: #1c1a1a;
    --sky: #6a67b8;
    --sea: #3cb3b0;
    --land: #e0a14e;
    --knot: #2a1c1a;
  }
  * { box-sizing: border-box; margin: 0; padding: 0; }
  html, body {
    width: 1200px;
    height: 1200px;
    overflow: hidden;
  }
  body {
    background: var(--paper);
  }
  .cover {
    position: relative;
    width: 1200px;
    height: 1200px;
    background:
      radial-gradient(ellipse at 30% 20%, var(--paper-shade) 0%, transparent 45%),
      radial-gradient(ellipse at 75% 80%, var(--paper-shade) 0%, transparent 40%),
      var(--paper);
    font-family: "Permanent Marker", cursive;
    color: var(--ink);
    text-transform: uppercase;
  }
  .artist-name {
    position: absolute;
    top: 38px;
    left: 0;
    width: 100%;
    text-align: center;
    font-size: 46px;
    line-height: 1.2;
    letter-spacing: 1px;
  }
  .album-title {
    position: absolute;
    top: 1080px;
    left: 0;
    width: 100%;
    text-align: center;
    font-size: 68px;
    line-height: 1.2;
    letter-spacing: 2px;
  }
  .realms-emblem {
    position: absolute;
    left: 168px;
    top: 120px;
    width: 872px;
    height: 896px;
    border-radius: 50%;
    background:
      radial-gradient(circle at 50% 28%, var(--sky) 0%, transparent 38%),
      radial-gradient(circle at 27% 72%, var(--sea) 0%, transparent 36%),
      radial-gradient(circle at 73% 72%, var(--land) 0%, transparent 36%),
      radial-gradient(circle at 50% 50%, var(--knot) 0%, #5a4a48 55%, var(--paper) 72%);
  }
</style>
</head>
<body>
  <main class="cover">
    <h2 class="artist-name">Oskar Venlow</h2>
    <div class="realms-emblem" role="img" aria-label="Painted Celtic triquetra knot inside a circle, its three lobes filled with sky violet, sea teal and amber land tones, each holding a spiral"></div>
    <h1 class="album-title">The Amber Tides</h1>
  </main>
</body>
</html>
```